Redesign lumenvale.com home page

We want to improve our website design overall, show us what you can do with our home page and we will move forward with the best designer to redo the other pages on our site.

Particularly interested in redesigning the header/footer.

Target Market(s)

scientists and engineers

Number of Pages Required

1 page

Font styles to use
Sans Serif

Requirements
Nice to have
• More grey and red and less black than we have now for the header

```html
<!DOCTYPE html>
<html lang="en">
<head>
<meta charset="utf-8">
<title>Lumenvale Corporation — Home</title>
<link href="https://fonts.googleapis.com/css2?family=Roboto:wght@400;500;700&family=Caveat:wght@500&display=swap" rel="stylesheet">
<style>
:root{
  --red:#cc1212;
  --ink:#222428;
  --text:#55585e;
  --muted:#8a8d93;
  --line:#e3e4e7;
  --grey-bg:#f3f4f6;
  --bar-bg:#eceef1;
  --white:#ffffff;
}
*{box-sizing:border-box;margin:0;padding:0}
html,body{width:1200px;height:2731px;overflow:hidden}
body{position:relative;background:var(--white);font-family:"Roboto",Arial,sans-serif;color:var(--text)}
.abs{position:absolute}

/* header */
.site-header{position:absolute;left:0;top:0;width:1200px;height:73px;background:var(--white);border-top:4px solid var(--red)}
.brand{position:absolute;display:flex;align-items:center;gap:10px;font-weight:700;color:var(--red);letter-spacing:1px}
.brand-mark{width:22px;height:22px;background:var(--red)}
.site-header .brand{left:47px;top:18px;font-size:20px}
.main-nav a{position:absolute;top:27px;font-size:14px;color:var(--ink);text-decoration:none;font-weight:500}
.header-contact{position:absolute;left:967px;top:27px;font-size:14px;color:var(--ink)}
.btn-quote{position:absolute;left:1032px;top:18px;width:122px;height:33px;background:var(--red);color:#fff;border-radius:5px;font-size:13px;font-weight:500;display:flex;align-items:center;justify-content:center}

/* hero */
.hero{position:absolute;left:0;top:73px;width:1200px;height:488px;
  background:
    radial-gradient(ellipse 420px 300px at 180px 240px,#5f7488 0%,transparent 70%),
    radial-gradient(ellipse 380px 260px at 520px 420px,#7a6a58 0%,transparent 70%),
    linear-gradient(110deg,#4e5e6c 0%,#5d6a5a 38%,#4d5a3e 62%,#5e6b48 82%,#6b705a 100%)}
.hero-shade{position:absolute;inset:0;background:rgba(20,24,28,.3)}
.hero-title{position:absolute;left:0;width:1200px;top:118px;text-align:center;font-family:"Caveat",cursive;font-size:52px;line-height:50px;color:#fff}
.hero-lead{position:absolute;left:200px;width:800px;top:258px;text-align:center;font-size:12.5px;line-height:18px;color:#fff}
.btn-outline{position:absolute;left:539px;top:331px;width:118px;height:33px;border:2px solid #fff;border-radius:6px;color:#fff;font-size:13px;font-weight:700;display:flex;align-items:center;justify-content:center}

/* contact bar */
.info-bar{position:absolute;left:0;top:561px;width:1200px;height:36px;background:var(--bar-bg);border-bottom:1px solid var(--line)}
.info-item{position:absolute;top:10px;font-size:13px;color:var(--muted);display:flex;align-items:center;gap:8px}
.social{position:absolute;top:9px;width:19px;height:19px;border-radius:3px}

/* section headings */
.section-title{position:absolute;left:0;width:1200px;text-align:center;font-size:23px;font-weight:500;color:var(--ink)}
.section-title em{font-style:normal;color:var(--red)}
.dotted{position:absolute;left:51px;width:1100px;border-top:2px dotted var(--red)}

.intro{position:absolute;left:55px;width:1092px;top:662px;text-align:center;font-size:12.5px;line-height:20px;color:var(--text)}

/* services */
.services{position:absolute;left:0;top:728px;width:1200px;height:303px;background:var(--grey-bg)}
.service-card{position:absolute;top:106px;width:255px;height:168px;border-radius:14px 0 14px 0;overflow:hidden}
.service-card .photo{height:126px}
.service-card .label{height:42px;background:var(--red);color:#fff;font-size:14px;font-weight:500;display:flex;align-items:center;justify-content:center}

/* mail form */
.mail{position:absolute;left:0;top:1031px;width:1200px;height:335px;background:linear-gradient(180deg,#6f8fb3 0%,#93aac4 45%,#b9c4cc 68%,#c7b27a 84%,#a58d55 100%)}
.mail .section-title{color:#fff;top:34px}
.field{position:absolute;height:31px;background:rgba(255,255,255,.45);border-radius:3px;font-size:12px;color:#fff;padding:9px 14px}
.btn-send{position:absolute;left:534px;top:273px;width:134px;height:31px;background:#fff;border-radius:3px;color:var(--ink);font-size:12px;font-weight:500;display:flex;align-items:center;justify-content:center}

/* what we do */
.accordion-item{position:absolute;left:615px;display:flex;align-items:center;gap:16px;font-size:16px;color:var(--ink)}
.chev{width:22px;height:22px;display:flex;align-items:center;justify-content:center}
.accordion-item.active{color:var(--red)}
.accordion-item.active .chev{background:var(--red);border-radius:3px}
.accordion-desc{position:absolute;left:653px;top:1509px;width:500px;font-size:13px;line-height:20px;color:var(--text)}

/* news */
.news{position:absolute;left:0;top:1894px;width:1200px;height:479px;background:var(--grey-bg)}
.news-card{position:absolute;top:87px;width:255px;height:355px;background:#fff}
.news-card .photo{height:191px}
.news-card h3{position:absolute;left:20px;top:211px;font-size:18px;font-weight:500;color:var(--ink)}
.news-card p{position:absolute;left:20px;top:241px;width:215px;font-size:13.5px;line-height:20px;color:var(--muted)}
.news-card .meta{position:absolute;left:20px;right:20px;top:318px;border-top:1px solid var(--line);padding-top:11px;font-size:11.5px;color:var(--muted);display:flex;justify-content:space-between}
.meta span{display:flex;align-items:center;gap:6px}

/* partners */
.partner{position:absolute;top:2449px;width:159px;height:106px}

/* footer */
.site-footer{position:absolute;left:0;top:2577px;width:1200px;height:154px;border-top:4px solid var(--red);background:#fff}
.foot-link{position:absolute;top:53px;font-size:13px;font-weight:500;color:var(--ink)}
.foot-sub{position:absolute;top:100px;font-size:11.5px;color:var(--text)}
.foot-rule{position:absolute;left:51px;width:1100px;top:80px;border-top:1px solid var(--line)}
.site-footer .brand{left:896px;top:36px;font-size:22px}
</style>
</head>
<body>

<header class="site-header">
  <div class="brand"><span class="brand-mark"></span>LUMENVALE</div>
  <nav class="main-nav">
    <a style="left:379px">Our Company</a>
    <a style="left:497px">Services</a>
    <a style="left:586px">Products</a>
    <a style="left:676px">News</a>
    <a style="left:743px">Applications</a>
  </nav>
  <div class="header-contact">Contact</div>
  <div class="btn-quote">Request a Quote</div>
</header>

<section class="hero" role="img" aria-label="Aerial photograph of rooftops beside green crop fields">
  <div class="hero-shade"></div>
  <h1 class="hero-title">Multispectral Technology<br>Advancement Industry Day</h1>
  <p class="hero-lead">Lumenvale Corporation's newest multispectral technology was demonstrated by the Northgate Defense Agency at<br>October's Hyper Spectral/Multi Spectral Technology Advancement Industry Day at Harlow Test Range, New Jersey.</p>
  <div class="btn-outline">READ MORE</div>
</section>

<div class="info-bar">
  <div class="info-item" style="left:51px">
    <svg width="12" height="12" viewBox="0 0 24 24"><path fill="#8a8d93" d="M6.6 10.8a15 15 0 0 0 6.6 6.6l2.2-2.2c.3-.3.7-.4 1-.2 1.1.4 2.3.6 3.6.6.6 0 1 .4 1 1V20c0 .6-.4 1-1 1A17 17 0 0 1 3 4c0-.6.4-1 1-1h3.5c.6 0 1 .4 1 1 0 1.3.2 2.5.6 3.6.1.3 0 .7-.2 1z"/></svg>
    +1 800 555 0142
  </div>
  <div class="info-item" style="left:209px">
    <svg width="13" height="10" viewBox="0 0 26 20"><rect width="26" height="20" rx="2" fill="#8a8d93"/><path d="M1 2l12 9 12-9" stroke="#eceef1" stroke-width="2" fill="none"/></svg>
    info@lumenvale.com
  </div>
  <span class="social" style="left:1009px;background:#4a66a8" aria-label="Social profile"></span>
  <span class="social" style="left:1048px;background:#d4553f" aria-label="Social profile"></span>
  <span class="social" style="left:1089px;background:#3d9fdc" aria-label="Social profile"></span>
  <svg class="abs" style="left:1132px;top:11px" width="14" height="14" viewBox="0 0 24 24"><circle cx="10" cy="10" r="7" stroke="#8a8d93" stroke-width="3" fill="none"/><path d="M15 15l7 7" stroke="#8a8d93" stroke-width="3"/></svg>
</div>

<h2 class="section-title" style="top:601px">Welcome to <em>Lumenvale Corporation</em></h2>
<div class="dotted" style="top:641px"></div>
<p class="intro">Lumenvale Corporation offers a single engineering and manufacturing source for characterization, control, and exploitation of the optical properties of surfaces. Our unique understanding of customers' needs allows us to offer engineering services, proprietary analytical software, reflectometers, hyperspectral and multispectral imagers, and surface coating products that are cost effective, innovative, and provide unsurpassed performance.</p>

<section class="services">
  <h2 class="section-title" style="top:17px">Our <em>Services</em></h2>
  <div class="dotted" style="top:59px"></div>
  <div class="service-card" style="left:51px">
    <div class="photo" role="img" aria-label="Vacuum coating chamber in a lab" style="background:linear-gradient(90deg,#4a4d52 0%,#9da2a6 22%,#d6d9db 55%,#a9aeb2 80%,#6d7277 100%)"></div>
    <div class="label">Coatings</div>
  </div>
  <div class="service-card" style="left:333px">
    <div class="photo" role="img" aria-label="Engineer surveying power line towers" style="background:linear-gradient(180deg,#e2e5e7 0%,#c6cacd 50%,#9a8f80 82%,#6f6558 100%)"></div>
    <div class="label">Measurement Services</div>
  </div>
  <div class="service-card" style="left:614px">
    <div class="photo" role="img" aria-label="Imaging panel against a sunset sky" style="background:linear-gradient(180deg,#2f3c52 0%,#56647a 40%,#b58a57 75%,#e0b06a 100%)"></div>
    <div class="label">Spectral Imaging Systems</div>
  </div>
  <div class="service-card" style="left:894px">
    <div class="photo" role="img" aria-label="Reflectometer instrument on a bench" style="background:radial-gradient(circle at 50% 45%,#3a3d41 0%,#6a6e72 30%,#d2d5d8 65%,#eceef0 100%)"></div>
    <div class="label">Reflectometers | Emissometers</div>
  </div>
</section>

<section class="mail" role="img" aria-label="Man in a hat looking over a wheat field under blue sky">
  <h2 class="section-title">Feel Free to Mail</h2>
  <div class="field" style="left:49px;top:76px;width:541px">Name *</div>
  <div class="field" style="left:610px;top:76px;width:541px">Email *</div>
  <div class="field" style="left:49px;top:127px;width:541px">Phone Number</div>
  <div class="field" style="left:610px;top:127px;width:541px">Subject</div>
  <div class="field" style="left:49px;top:178px;width:1102px;height:73px">Write Your Message Here...</div>
  <div class="btn-send">SEND MESSAGE</div>
</section>

<h2 class="section-title" style="top:1377px">What <em>We Do</em></h2>
<div class="dotted" style="top:1417px"></div>
<svg class="abs" style="left:51px;top:1453px" width="535" height="412" viewBox="0 0 535 412" role="img" aria-label="Aerial view of a tower block under construction with a camera drone">
  <defs>
    <linearGradient id="siteTone" x1="0" y1="0" x2="1" y2="1">
      <stop offset="0" stop-color="#7d8478"/>
      <stop offset=".45" stop-color="#9aa0a3"/>
      <stop offset=".75" stop-color="#6e6a5c"/>
      <stop offset="1" stop-color="#4b4a42"/>
    </linearGradient>
  </defs>
  <polygon points="0,0 535,0 213,412 0,412" fill="url(#siteTone)"/>
</svg>

<div class="accordion-item active" style="top:1479px">
  <span class="chev"><svg width="10" height="6" viewBox="0 0 10 6"><path d="M1 5l4-4 4 4" stroke="#fff" stroke-width="1.6" fill="none"/></svg></span>R&amp;D Engineering Services
</div>
<p class="accordion-desc">Expert support for projects in optical phenomenology and measurements, and development of customized instruments and accessories for specific measurement applications</p>
<div class="accordion-item" style="top:1595px"><span class="chev"><svg width="10" height="6" viewBox="0 0 10 6"><path d="M1 1l4 4 4-4" stroke="#cc1212" stroke-width="1.6" fill="none"/></svg></span>Hyperspectral and Multispectral Imaging</div>
<div class="accordion-item" style="top:1652px"><span class="chev"><svg width="10" height="6" viewBox="0 0 10 6"><path d="M1 1l4 4 4-4" stroke="#cc1212" stroke-width="1.6" fill="none"/></svg></span>Optical Properties Measurements</div>
<div class="accordion-item" style="top:1708px"><span class="chev"><svg width="10" height="6" viewBox="0 0 10 6"><path d="M1 1l4 4 4-4" stroke="#cc1212" stroke-width="1.6" fill="none"/></svg></span>Vacuum Deposition Coatings</div>
<div class="accordion-item" style="top:1765px"><span class="chev"><svg width="10" height="6" viewBox="0 0 10 6"><path d="M1 1l4 4 4-4" stroke="#cc1212" stroke-width="1.6" fill="none"/></svg></span>Reflectometer Instrumentation</div>
<div class="accordion-item" style="top:1819px"><span class="chev"><svg width="10" height="6" viewBox="0 0 10 6"><path d="M1 1l4 4 4-4" stroke="#cc1212" stroke-width="1.6" fill="none"/></svg></span>Pigmented Coatings</div>

<section class="news">
  <h2 class="section-title" style="top:15px">Latest <em>News &amp; Views</em></h2>
  <div class="dotted" style="top:55px"></div>
  <article class="news-card" style="left:51px">
    <div class="photo" role="img" aria-label="Traveller with a bag walking through a doorway" style="background:linear-gradient(90deg,#cfcac2 0%,#a89e92 40%,#7b5434 70%,#5a3a22 100%)"></div>
    <h3>Standard Post</h3>
    <p>Enim congue blandit. Lorem ipsum dolor sit amet, consectetur adipiscing elit. Quisque...</p>
    <div class="meta">
      <span><svg width="10" height="10" viewBox="0 0 10 10"><rect x="0.5" y="1.5" width="9" height="8" fill="none" stroke="#8a8d93"/><rect x="0.5" y="1.5" width="9" height="2.5" fill="#8a8d93"/></svg>22 June, 2015</span>
      <span><svg width="11" height="10" viewBox="0 0 11 10"><path d="M1 1h9v6H4l-3 2.5z" fill="#8a8d93"/></svg>0</span>
    </div>
  </article>
  <article class="news-card" style="left:333px">
    <div class="photo" role="img" aria-label="Glass coffee carafe on a table" style="background:linear-gradient(180deg,#cfc9bf 0%,#b9ad9a 55%,#8c7a5e 80%,#6a5a44 100%)"></div>
    <h3>Video Post</h3>
    <p>Ultrices posuere cubilia curae curabitur sit amet tortor ut massa commodo. Vestibulum...</p>
    <div class="meta">
      <span><svg width="10" height="10" viewBox="0 0 10 10"><rect x="0.5" y="1.5" width="9" height="8" fill="none" stroke="#8a8d93"/><rect x="0.5" y="1.5" width="9" height="2.5" fill="#8a8d93"/></svg>22 June, 2015</span>
      <span><svg width="11" height="10" viewBox="0 0 11 10"><path d="M1 1h9v6H4l-3 2.5z" fill="#8a8d93"/></svg>0</span>
    </div>
  </article>
  <article class="news-card" style="left:614px">
    <div class="photo" role="img" aria-label="Cafe table and chair against a brick wall" style="background:linear-gradient(180deg,#6e4330 0%,#8e5a40 45%,#c8ae88 75%,#a88c62 100%)"></div>
    <h3>Post with Image</h3>
    <p>Enim congue blandit. Lorem ipsum dolor sit amet, consectetur adipiscing elit. Quisque...</p>
    <div class="meta">
      <span><svg width="10" height="10" viewBox="0 0 10 10"><rect x="0.5" y="1.5" width="9" height="8" fill="none" stroke="#8a8d93"/><rect x="0.5" y="1.5" width="9" height="2.5" fill="#8a8d93"/></svg>22 June, 2015</span>
      <span><svg width="11" height="10" viewBox="0 0 11 10"><path d="M1 1h9v6H4l-3 2.5z" fill="#8a8d93"/></svg>0</span>
    </div>
  </article>
  <article class="news-card" style="left:894px">
    <div class="photo" role="img" aria-label="Leather wallet on a wooden surface" style="background:radial-gradient(ellipse 120px 70px at 50% 60%,#6e4a30 0%,#9a7a5a 55%,transparent 80%),linear-gradient(135deg,#dcd6cb,#b3a794)"></div>
    <h3>Image Post</h3>
    <p>Ultrices posuere cubilia curae curabitur sit amet tortor ut massa commodo. Vestibulum...</p>
    <div class="meta">
      <span><svg width="10" height="10" viewBox="0 0 10 10"><rect x="0.5" y="1.5" width="9" height="8" fill="none" stroke="#8a8d93"/><rect x="0.5" y="1.5" width="9" height="2.5" fill="#8a8d93"/></svg>22 June, 2015</span>
      <span><svg width="11" height="10" viewBox="0 0 11 10"><path d="M1 1h9v6H4l-3 2.5z" fill="#8a8d93"/></svg>3</span>
    </div>
  </article>
</section>

<h2 class="section-title" style="top:2386px">Trusted by More <em>Than 5,000 Organisations</em></h2>
<div class="dotted" style="top:2426px"></div>
<div class="partner" style="left:51px;background:linear-gradient(135deg,#7a8896,#4e5b68)" role="img" aria-label="Partner organisation"></div>
<div class="partner" style="left:240px;background:linear-gradient(135deg,#55585f,#303238)" role="img" aria-label="Partner organisation"></div>
<div class="partner" style="left:428px;background:linear-gradient(135deg,#4f4640,#2c2724)" role="img" aria-label="Partner organisation"></div>
<div class="partner" style="left:616px;background:linear-gradient(135deg,#3b3e43,#1f2124)" role="img" aria-label="Partner organisation"></div>
<div class="partner" style="left:804px;background:linear-gradient(135deg,#a5abb1,#70767d)" role="img" aria-label="Partner organisation"></div>
<div class="partner" style="left:992px;background:linear-gradient(135deg,#8ea7bd,#5c7891)" role="img" aria-label="Partner organisation"></div>

<footer class="site-footer">
  <svg class="abs" style="left:60px;top:55px" width="13" height="13" viewBox="0 0 24 24"><circle cx="10" cy="10" r="7" stroke="#222428" stroke-width="3" fill="none"/><path d="M15 15l7 7" stroke="#222428" stroke-width="3"/></svg>
  <span class="foot-link" style="left:95px">Help &amp; Contact</span>
  <span class="foot-link" style="left:211px">Products</span>
  <span class="foot-link" style="left:291px">Services</span>
  <span class="foot-link" style="left:370px">Applications</span>
  <span class="foot-link" style="left:472px">Shop</span>
  <div class="brand"><span class="brand-mark"></span>LUMENVALE</div>
  <div class="foot-rule"></div>
  <span class="foot-sub" style="left:60px">About</span>
  <span class="foot-sub" style="left:111px">Blog</span>
  <span class="foot-sub" style="left:153px">Jobs</span>
  <span class="foot-sub" style="left:199px">Our Team</span>
  <span class="foot-sub" style="left:268px">Public Policy</span>
  <span class="foot-sub" style="left:353px">Sitemap</span>
  <span class="foot-sub" style="left:417px">Facilities</span>
  <span class="foot-sub" style="left:481px">Partners</span>
  <span class="foot-sub" style="left:896px">© 2015–2017</span>
  <span class="foot-sub" style="left:985px">Privacy</span>
  <span class="foot-sub" style="left:1043px">Legal</span>
  <span class="foot-sub" style="left:1091px">Feedback</span>
</footer>

</body>
</html>
```